Nutrition data company website needs a new look

Our company is a B2B food database. We focus on nutrition and related health data like full nutrition profiles, product sourcing and packaging. Our goal is to provide the data that can help companies unleash their creativity to offer better foods and products.

Redesign our website to avoid food cliches. Every website that is interested in understanding health shows avocados, berries and salads. What can we do differently?

Take a look at our website

Plumtrel.ai

We like the look BUT we want to get away from typical food images. So…

Create the conceptual look for our website. What’s the visual hook? What’s a different visual style that could be interesting? Is it images of people that’s connected to food or data but not just typical stock photography? Is it an illustration style that brings everything to life? Is it more technical looking but still very human?

Be conceptual. Take some risks. We are open to very different ideas. It doesn’t mean you can’t use food. Just don’t look like every other health and nutrition site! Don’t just show typical stock photos.

WHAT WE LOVE ABOUT OUR CURRENT WEBSITE

It’s clean and simple. We like our logo and “blue” color. It human and not business or techy. You can use white space if you like, but don't have to.

WHAT WE DON’T LIKE

The use of food or people cliches

So the biggest asks are to avoid cliches and typical imagery. And don’t be too ‘visually busy’. We like a clean look. But surprise us!

Remember the customer is B2B but don’t be afraid to take any risks. Must look good on mobile too!
Updates

Need extra days to review

Hi. We will be making a decision shortly. Thank you all for all your hard work. You've all made this a difficult decision!

Target Market(s)

B2B customers, food manufacturers, food retailers, restaurants, food scientists etc

Industry/Entity Type

Data and food

Number of Pages Required

1 page

Font styles to use
Sans Serif
Other font styles liked:
• Montserrat, Proximanova but others too

Colors
0094D4
00A9DD
6FCCEA
C7EBF8
E9F6FB

Requirements
Must have
• Don't be cliche
Nice to have
• Simple clean look
Should not have
• Typical food or people stock imagery

```html
<!DOCTYPE html>
<html lang="en">
<head>
<meta charset="utf-8">
<title>Plumtrel — Truth in Nutritions</title>
<link href="https://fonts.googleapis.com/css2?family=Poppins:wght@300;400;500;600;700&family=Roboto:wght@300;400;500&display=swap" rel="stylesheet">
<style>
  :root {
    --blue-deep: #0094d4;
    --blue: #00a9dd;
    --blue-mid: #40b6dc;
    --blue-soft: #6fccea;
    --blue-pale: #c7ebf8;
    --blue-mist: #e9f6fb;
    --ink: #1e1e1e;
    --text: #333333;
    --muted: #6b6b6b;
    --band: #f7f7f7;
    --field: #ececec;
    --white: #ffffff;
  }
  * { box-sizing: border-box; margin: 0; padding: 0; }
  html, body { width: 1200px; height: 3802px; overflow: hidden; }
  body { position: relative; background: var(--white); font-family: "Roboto", Arial, sans-serif; color: var(--text); }

  .blob { position: absolute; border-radius: 50%; background: var(--blue-pale); filter: blur(40px); opacity: .8; }

  /* Hero */
  .hero { position: absolute; left: 0; top: 0; width: 1200px; height: 658px; background: var(--band); overflow: hidden; }
  .brand { position: absolute; left: 117px; top: 24px; font-family: "Poppins", sans-serif; font-weight: 600; font-size: 36px; color: var(--blue); letter-spacing: -.5px; }
  .nav { position: absolute; top: 36px; right: 0; width: 1200px; font-family: "Poppins", sans-serif; font-weight: 300; font-size: 15px; color: var(--ink); }
  .nav a { position: absolute; color: inherit; text-decoration: none; }
  .hero-title { position: absolute; left: 117px; top: 232px; font-family: "Poppins", sans-serif; font-weight: 600; font-size: 84px; line-height: 90px; color: var(--ink); letter-spacing: -1px; }
  .hero-title .accent { color: var(--blue); }
  .hero-sub { position: absolute; left: 117px; top: 441px; font-family: "Poppins", sans-serif; font-size: 22px; color: var(--ink); }
  .hero-visual { position: absolute; left: 640px; top: 148px; width: 560px; height: 510px; border-radius: 260px 0 0 0;
    background: radial-gradient(circle at 45% 30%, #58c35a 0 22%, transparent 23%), radial-gradient(ellipse at 70% 85%, #e8b89c 0 30%, transparent 31%), linear-gradient(160deg, var(--blue-mist), var(--blue-pale)); }
  .chip { position: absolute; background: var(--white); border-radius: 6px; box-shadow: 0 4px 14px rgba(0,0,0,.08); }
  .chip-icon { left: 614px; top: 196px; width: 55px; height: 55px; display: flex; align-items: center; justify-content: center; }
  .chip-chart { left: 860px; top: 337px; width: 154px; height: 103px; padding: 10px 12px; }
  .chip-chart span { font-size: 11px; color: var(--ink); font-family: "Poppins", sans-serif; }

  /* Calories */
  .kcal-visual { position: absolute; left: 117px; top: 782px; width: 208px; height: 416px; border-radius: 208px 0 0 208px;
    background: radial-gradient(circle at 80% 50%, #8bbd45, #3d5a2a 60%, #2a3550); border: 5px solid #e2e2e2; border-right: none; }
  .kcal-ring { position: absolute; left: 117px; top: 782px; }
  .kcal-label { position: absolute; left: 341px; top: 928px; font-family: "Poppins", sans-serif; font-size: 36px; color: var(--ink); }
  .kcal-value { position: absolute; left: 341px; top: 982px; font-family: "Poppins", sans-serif; font-weight: 600; font-size: 54px; color: var(--ink); }
  .intro { position: absolute; left: 614px; top: 866px; width: 470px; font-weight: 300; font-size: 25px; line-height: 46px; color: var(--text); }

  /* Pillars */
  .pillar { position: absolute; top: 1322px; width: 340px; text-align: center; }
  .pillar h3 { font-family: "Poppins", sans-serif; font-weight: 600; font-size: 40px; color: var(--ink); }
  .pillar p { margin-top: 14px; font-weight: 500; font-size: 20px; line-height: 33px; color: var(--ink); }
  .pillar .icon { margin: 40px auto 0; width: 126px; height: 126px; border-radius: 50%; }

  /* Power of data */
  .power { position: absolute; left: 0; top: 1757px; width: 1200px; height: 388px; background: var(--band); overflow: hidden; text-align: center; }
  .section-title { font-family: "Poppins", sans-serif; font-weight: 600; font-size: 46px; color: var(--ink); }
  .section-title .accent { color: var(--blue); }
  .power .section-title { position: absolute; top: 62px; width: 100%; }
  .power p { position: absolute; left: 190px; top: 145px; width: 820px; font-weight: 300; font-size: 25px; line-height: 46px; color: var(--text); }

  /* Team */
  .team-title { position: absolute; top: 2270px; width: 1200px; text-align: center; }
  .team-text { position: absolute; left: 120px; top: 2352px; width: 960px; text-align: center; font-size: 16px; line-height: 30px; color: var(--muted); }
  .team-visual { position: absolute; left: 360px; top: 2435px; width: 477px; height: 319px; border-radius: 140px 200px 40px 140px;
    background: linear-gradient(135deg, var(--blue-mist), var(--blue-pale) 60%, #d9eef7); }
  .btn { position: absolute; display: flex; align-items: center; justify-content: center; background: var(--blue-mid); color: var(--white); border-radius: 8px; font-size: 15px; }
  .btn-positions { left: 499px; top: 2819px; width: 199px; height: 53px; }

  /* Contact */
  .contact { position: absolute; left: 0; top: 2999px; width: 1200px; height: 803px; background: var(--band); overflow: hidden; }
  .contact .section-title { position: absolute; top: 50px; width: 100%; text-align: center; line-height: 67px; }
  .contact-sub { position: absolute; top: 3193px; width: 1200px; text-align: center; font-weight: 300; font-size: 25px; color: var(--ink); }
  .form-card { position: absolute; left: 365px; top: 3250px; width: 470px; height: 465px; background: var(--white); border-radius: 30px; box-shadow: 0 4px 24px rgba(0,0,0,.06); }
  .field { position: absolute; left: 25px; width: 420px; height: 53px; background: var(--field); border-radius: 12px; padding: 15px 29px; font-size: 16px; color: #9a9a9a; }
  .btn-submit { left: 25px; top: 387px; width: 420px; height: 53px; border-radius: 12px; font-size: 18px; }
  .footer { position: absolute; top: 3774px; width: 1200px; text-align: center; font-size: 12px; color: var(--muted); }
</style>
</head>
<body>

<header class="hero">
  <div class="blob" style="left:1020px;top:-60px;width:220px;height:220px"></div>
  <div class="blob" style="left:-90px;top:150px;width:220px;height:220px"></div>
  <div class="brand">Plumtrel</div>
  <nav class="nav">
    <a style="left:807px">Home</a>
    <a style="left:911px">Career</a>
    <a style="left:1021px">Contact</a>
  </nav>
  <h1 class="hero-title">Truth in<br><span class="accent">Nutritions</span></h1>
  <p class="hero-sub">Food and beverage data and insights</p>
  <div class="hero-visual" role="img" aria-label="Photo of two green juice cartons floating above an open hand"></div>
  <div class="chip chip-icon">
    <svg width="32" height="32" viewBox="0 0 32 32" fill="none" stroke="#00a9dd" stroke-width="1.6">
      <circle cx="16" cy="16" r="2.5" fill="#00a9dd"/>
      <ellipse cx="16" cy="16" rx="13" ry="5"/>
      <ellipse cx="16" cy="16" rx="13" ry="5" transform="rotate(60 16 16)"/>
      <ellipse cx="16" cy="16" rx="13" ry="5" transform="rotate(-60 16 16)"/>
    </svg>
  </div>
  <div class="chip chip-chart">
    <span>Nutritions</span>
    <svg width="130" height="60" viewBox="0 0 130 60">
      <g fill="#40b6dc">
        <rect x="2" y="30" width="5" height="30" rx="2"/><rect x="14" y="44" width="5" height="16" rx="2"/>
        <rect x="26" y="50" width="5" height="10" rx="2"/><rect x="38" y="36" width="5" height="24" rx="2"/>
        <rect x="50" y="24" width="5" height="36" rx="2"/><rect x="62" y="42" width="5" height="18" rx="2"/>
        <rect x="74" y="18" width="5" height="42" rx="2"/><rect x="86" y="28" width="5" height="32" rx="2"/>
        <rect x="98" y="14" width="5" height="46" rx="2"/><rect x="110" y="22" width="5" height="38" rx="2"/>
        <rect x="122" y="20" width="5" height="40" rx="2"/>
      </g>
    </svg>
  </div>
</header>

<section class="calories">
  <div class="kcal-visual" role="img" aria-label="Photo of a bowl of green smoothie topped with blueberries, mango and herbs"></div>
  <svg class="kcal-ring" width="430" height="420" viewBox="0 0 430 420">
    <defs><linearGradient id="ring" x1="0" y1="0" x2="0" y2="1"><stop offset="0" stop-color="#6fccea"/><stop offset="1" stop-color="#40b6dc"/></linearGradient></defs>
    <path d="M226 10 A200 200 0 0 1 226 408" fill="none" stroke="url(#ring)" stroke-width="20" stroke-linecap="round"/>
  </svg>
  <div class="kcal-label">Kcal</div>
  <div class="kcal-value">272.7</div>
  <p class="intro">Simply put, food data is inaccurate, incomplete, and outdated. Plumtrel develops the data, insights, and tools that bring food and beverage information into the 21st century.</p>
</section>

<section class="pillars">
  <div class="pillar" style="left:99px">
    <h3>Science</h3>
    <p>Pioneering research and<br>discovery</p>
    <div class="icon" role="img" aria-label="Atom icon" style="background:radial-gradient(circle,#e03a4f 0 14%,#c7ebf8 15% 60%,transparent 61%)"></div>
  </div>
  <div class="pillar" style="left:430px">
    <h3>Industry</h3>
    <p>Driving innovation<br>and differentiation</p>
    <div class="icon" role="img" aria-label="Light bulb icon" style="background:radial-gradient(circle,#ffd11a 0 40%,#fff3c4 41% 60%,transparent 61%)"></div>
  </div>
  <div class="pillar" style="left:760px">
    <h3>Consumers</h3>
    <p>Informing better choices and<br>better health</p>
    <div class="icon" role="img" aria-label="Hands holding a heart icon" style="background:radial-gradient(circle,#ef4f5f 0 30%,#fcd6c0 31% 60%,transparent 61%)"></div>
  </div>
</section>

<section class="power">
  <div class="blob" style="left:440px;top:-40px;width:180px;height:180px"></div>
  <div class="blob" style="left:-80px;top:150px;width:200px;height:200px"></div>
  <div class="blob" style="left:1100px;top:40px;width:180px;height:180px"></div>
  <div class="blob" style="left:860px;top:230px;width:200px;height:200px"></div>
  <h2 class="section-title">The Power of Data</h2>
  <p>Plumtrel is dedicated to providing critical and actionable information and insights. We relentlessly pursue the potential of data to help the world make better decisions, have better outcomes and improve the health and well-being of every one of us.</p>
</section>

<section class="team">
  <h2 class="section-title team-title">Join Our <span class="accent">Team</span></h2>
  <p class="team-text">Lorem ipsum dolor sit amet, consectetur adipiscing elit. Donec id congue augue, vitae convallis enim. Ut volutpat dapibus volutpat. Donec eu ante elit.</p>
  <div class="team-visual" role="img" aria-label="Illustration of two colleagues cheering at a shared desk with a laptop"></div>
  <a class="btn btn-positions">See Open Position</a>
</section>

<section class="contact">
  <div class="blob" style="left:120px;top:100px;width:200px;height:200px"></div>
  <div class="blob" style="left:1000px;top:20px;width:260px;height:260px"></div>
  <div class="blob" style="left:780px;top:270px;width:200px;height:200px"></div>
  <div class="blob" style="left:-80px;top:560px;width:240px;height:240px"></div>
  <div class="blob" style="left:850px;top:560px;width:200px;height:200px"></div>
  <h2 class="section-title">Work with, partner<br>with, or join us</h2>
</section>
<p class="contact-sub">We’d love to hear from you</p>
<form class="form-card">
  <div class="field" style="top:25px">Name</div>
  <div class="field" style="top:100px">Email</div>
  <div class="field" style="top:176px">Subject</div>
  <div class="field" style="top:251px;height:114px">Message</div>
  <div class="btn btn-submit">Submit</div>
</form>
<footer class="footer">© 2021 by Plumtrel llc. All rights reserved.</footer>

</body>
</html>
```